electrical company- Company name- Voltmark Trades, slogan- All installations and servicingcolours to stick roughly with logo- greys, blues, black, white. simple yet effective- logo to stand out and attention to name also (gareth). Modern design.

Industry/Entity Type

Business

Contact Information for Business Card

gareth WilliamsElectrician021 994 306info@voltmarktrades.co.nzwww.voltmarktrades.co.nzPO box 5367Palmerston North, 4472

```html
<!DOCTYPE html>
<html lang="en">
<head>
<meta charset="utf-8">
<title>Voltmark Trades – Business Cards</title>
<link rel="stylesheet" href="https://fonts.googleapis.com/css2?family=Open+Sans:wght@400;600;700&display=swap">
<style>
  :root {
    --backdrop: #3a322e;
    --card-dark: #1f2022;
    --card-blue: #2b9fdc;
    --accent-blue: #2a9bd8;
    --text-light: #d9d9d9;
    --text-white: #ffffff;
    --divider: rgba(255,255,255,0.08);
  }
  html, body {
    margin: 0;
    padding: 0;
    width: 1200px;
    height: 844px;
    overflow: hidden;
    background: var(--backdrop);
    font-family: "Open Sans", sans-serif;
  }
  .canvas {
    position: relative;
    width: 1200px;
    height: 844px;
  }
  .card {
    position: absolute;
    top: 267px;
    width: 520px;
    height: 310px;
    border-radius: 3px;
    box-shadow: 0 10px 28px rgba(0,0,0,0.45);
    overflow: hidden;
  }
  /* Contact side */
  .card--contact {
    left: 50px;
    background: var(--card-dark);
  }
  .card--contact .brand {
    position: absolute;
    left: 0;
    top: 0;
    width: 246px;
    height: 310px;
    display: flex;
    align-items: center;
    justify-content: center;
    gap: 9px;
  }
  .brand-square {
    width: 20px;
    height: 20px;
    background: var(--accent-blue);
    flex: none;
  }
  .brand-name {
    font-weight: 700;
    font-size: 21px;
    letter-spacing: 0.3px;
    color: var(--accent-blue);
    white-space: nowrap;
  }
  .card--contact .divider {
    position: absolute;
    left: 252px;
    top: 40px;
    width: 1px;
    height: 230px;
    background: var(--divider);
  }
  .details {
    position: absolute;
    left: 268px;
    right: 14px;
    top: 64px;
    color: var(--text-light);
    font-size: 12px;
    line-height: 17px;
  }
  .details .person-name {
    color: var(--accent-blue);
    font-size: 16px;
    font-weight: 600;
    line-height: 20px;
  }
  .details .role { margin-bottom: 18px; }
  .details .address { margin-bottom: 18px; }
  .contact-line {
    display: flex;
    align-items: center;
    gap: 7px;
    white-space: nowrap;
  }
  .contact-line svg { width: 10px; height: 10px; flex: none; fill: var(--accent-blue); }

  /* Brand side */
  .card--brand {
    left: 630px;
    background: var(--card-blue);
    color: var(--text-white);
    display: flex;
    flex-direction: column;
    align-items: center;
    justify-content: center;
    gap: 14px;
  }
  .card--brand .brand-row {
    display: flex;
    align-items: center;
    gap: 12px;
  }
  .card--brand .brand-square { background: var(--text-white); width: 26px; height: 26px; }
  .card--brand .brand-name { color: var(--text-white); font-size: 28px; }
  .slogan {
    font-size: 13px;
    color: var(--text-white);
  }
</style>
</head>
<body>
<main class="canvas">

  <section class="card card--contact">
    <div class="brand">
      <span class="brand-square"></span>
      <span class="brand-name">Voltmark Trades</span>
    </div>
    <div class="divider"></div>
    <div class="details">
      <div class="person-name">Gareth Pemberly</div>
      <div class="role">Electrician</div>
      <div class="address">PO box 8142<br>Palmerston North, 4472</div>
      <div class="contact-line">
        <svg viewBox="0 0 10 10" aria-hidden="true"><path d="M1 2.5C1 1.5 2 1 3 1l1 2-1 1c.6 1.2 1.8 2.4 3 3l1-1 2 1c0 1-.5 2-1.5 2C4.5 9 1 5.5 1 2.5z"/></svg>
        <span>021 573 814</span>
      </div>
      <div class="contact-line">
        <svg viewBox="0 0 10 10" aria-hidden="true"><rect x="0.5" y="2" width="9" height="6.5" rx="0.8"/></svg>
        <span>info@voltmarktrades-example.co.nz</span>
      </div>
      <div class="contact-line">
        <svg viewBox="0 0 10 10" aria-hidden="true"><path d="M2 8.5 4.5 6M5.5 4 8 1.5" stroke="#2a9bd8" stroke-width="1.6" fill="none"/><circle cx="5" cy="5" r="1.6"/></svg>
        <span>www.voltmarktrades-example.co.nz</span>
      </div>
    </div>
  </section>

  <section class="card card--brand">
    <div class="brand-row">
      <span class="brand-square"></span>
      <span class="brand-name">Voltmark Trades</span>
    </div>
    <div class="slogan">All Installations and Servicing</div>
  </section>

</main>
</body>
</html>
```